Website Design

This is a Website design project for a Software Developer / Consulting Company called Quillmarsh.

I would like to have a place for : blogs, partners, products, solutions and whatever you recommend. It would be nice to have a slot for Case Studies and Video Training.

I like our Competitor's site www.vornelix.example
I DO NOT LIKE our competitor's MAIN Page: www.trelvani.example.
Although Trelvani does have a nice way of putting blog news and twitter. below their webpage.

There should be a place for us to change our Logo: i.e. Like ZUMBRO. EVeryday zumbro changes its logo color.

thanks

Farid
Updates

Deisgns look good. However, I would like to see more deisgn options. Please be a little creative. thank you

Farid

Reason: We need to do some more modifications. We will be narrowing down the selections and working with Designers to get it to final stage.

Industry/Entity Type

It Company

```html
<!DOCTYPE html>
<html lang="en">
<head>
<meta charset="utf-8">
<title>Quillmarsh – Home</title>
<link rel="stylesheet" href="https://fonts.googleapis.com/css2?family=Aldrich&family=Arimo:wght@400;700&display=swap">
<style>
:root{
  --orange:#f47a30;
  --orange-dark:#d9621c;
  --peach:#fde5d6;
  --peach-light:#fdeee4;
  --ink:#2a2a2a;
  --link:#3b5bb5;
  --bar:#4a4a4a;
  --footer:#1b1b1b;
  --footer-bottom:#2a2a2a;
  --white:#ffffff;
}
*{margin:0;padding:0;box-sizing:border-box}
html,body{width:900px;height:1200px;overflow:hidden;background:var(--white)}
body{position:relative;font-family:"Arimo",Arial,sans-serif;color:var(--ink)}
.abs{position:absolute}
.display{font-family:"Aldrich",sans-serif}

/* header */
.brand{left:170px;top:28px;display:flex;align-items:center;gap:8px;font-family:"Aldrich",sans-serif;font-size:25px;color:var(--ink)}
.brand-mark{width:30px;height:30px;border-radius:50%;background:var(--orange)}
.main-nav{left:408px;top:55px;display:flex;gap:13px;font-family:"Aldrich",sans-serif;font-size:10px;letter-spacing:.6px;color:var(--ink)}
.main-nav span:last-child{margin-left:8px}
.top-bar{left:97px;top:78px;width:719px;height:28px;background:var(--bar)}

/* hero */
.hero{left:97px;top:106px;width:719px;height:302px;overflow:hidden;
  background:linear-gradient(180deg,#4f83c9 0%,#8ab4e0 38%,#2aa6c6 46%,#e9eef2 58%,#f4f6f8 100%)}
.hero-prev{left:-60px;top:84px;width:120px;height:132px;border-radius:50%;background:rgba(90,90,90,.55)}
.hero-prev svg{position:absolute;right:20px;top:48px}
.hero-title{left:141px;top:40px;color:var(--white);font-size:40px;line-height:44px}
.hero-sub{left:141px;top:88px;color:var(--white);font-size:31px}
.btn{background:var(--orange);color:var(--white);font-family:"Aldrich",sans-serif;border-radius:8px;
  box-shadow:0 3px 0 var(--orange-dark);display:flex;align-items:center;justify-content:center}
.btn-register{left:143px;top:126px;width:122px;height:33px;font-size:16px}
.hero-dots{left:314px;top:283px;display:flex;gap:8px}
.hero-dots i{width:9px;height:9px;border-radius:50%;background:#555}
.hero-dots i:first-child{background:var(--white)}

/* welcome */
.welcome-title{left:168px;top:432px;font-size:21px;color:var(--orange)}
.body-copy{font-size:10.5px;line-height:12.2px}
.welcome-copy{left:168px;top:464px;width:310px}
.btn-order{left:168px;top:564px;width:147px;height:38px;font-size:19px;border-radius:10px}

.cases{left:502px;top:408px;width:314px;height:217px;background:var(--peach)}
.cases-head{height:29px;background:var(--orange);color:var(--white);font-size:18px;padding:4px 0 0 15px}
.cases-copy{left:23px;top:41px;width:245px}
.read-more{display:inline-block;background:var(--orange);color:var(--white);font-size:6px;padding:2px 5px;border-radius:4px;vertical-align:middle}
.cases-rule{left:23px;top:106px;width:271px;height:1px;background:#555}
.cases-list{left:25px;top:116px;list-style:none}
.cases-list li{display:flex;align-items:center;gap:8px;height:23px;font-size:10.5px}
.cases-list li::before{content:"";width:9px;height:9px;border-radius:50%;background:var(--orange)}
.link{color:var(--link);text-decoration:underline}

/* products */
.products{left:97px;top:625px;width:719px;height:226px;background:var(--peach-light);box-shadow:inset 0 6px 6px -4px rgba(0,0,0,.25)}
.products-title{left:92px;top:24px;font-size:18px;color:var(--orange)}
.product-badge{width:106px;height:106px;border-radius:50%;border:4px solid var(--orange);background:var(--white);
  box-shadow:3px 4px 5px rgba(0,0,0,.3);display:flex;align-items:center;justify-content:center;
  font-weight:700;font-size:15px;color:var(--orange)}
.product-caption{width:200px}

/* video */
.video{left:184px;top:874px;width:283px;height:167px;background:#1c1c1c}
.video-controls{left:0;bottom:0;width:100%;height:13px;background:#0d0d0d;border-top:2px solid #444}
.media-title{left:495px;top:878px;font-size:17px;color:var(--orange)}
.media-copy{left:495px;top:903px;width:300px}
.media-rule{left:495px;top:935px;width:290px;height:1px;background:#555}
.demo-label{font-size:9px;color:var(--orange-dark)}
.demo-link{display:flex;align-items:center;gap:9px;font-size:10.5px;margin:3px 0 13px 7px}
.demo-link::before{content:"";width:7px;height:7px;background:var(--ink)}

/* footer */
.footer{left:97px;top:1063px;width:719px;height:100px;background:var(--footer);color:var(--white)}
.footer-title{left:54px;top:12px;font-size:12px}
.partner-card{width:92px;height:43px;background:var(--white);border-radius:6px;border:2px solid #ccc;
  display:flex;align-items:center;justify-content:center;color:#2a5db0;font-weight:700;font-size:13px}
.partner-info{font-size:8px;line-height:10px;width:100px}
.partner-info .link{color:#6f9be0}
.footer-divider{width:1px;height:65px;top:24px;background:#777}
.footer-bottom{left:97px;top:1163px;width:719px;height:37px;background:var(--footer-bottom);color:#ddd}
.copyright{left:205px;top:13px;font-size:10px}
.follow{left:386px;top:10px;font-size:13px;color:var(--orange)}
.follow-rule{left:457px;top:5px;width:2px;height:26px;background:var(--orange)}
.social{top:10px;width:17px;height:17px;border-radius:3px}
</style>
</head>
<body>

<header>
  <div class="abs brand"><span class="brand-mark"></span>Quillmarsh</div>
  <nav class="abs main-nav"><span>Products</span><span>Partners</span><span>Solutions</span><span>Support</span><span>Blogs</span><span>About Us</span></nav>
  <div class="abs top-bar"></div>
</header>

<section class="abs hero" role="img" aria-label="Photo of a tropical beach with palm trees, a thatched umbrella and a wooden lounger">
  <div class="abs hero-prev"><svg width="22" height="36" viewBox="0 0 22 36"><polyline points="19,2 3,18 19,34" fill="none" stroke="#9a9a9a" stroke-width="3"/></svg></div>
  <div class="abs hero-title">Lorem ipsum</div>
  <div class="abs hero-sub">dolor sit amet</div>
  <div class="abs btn btn-register">Register</div>
  <div class="abs hero-dots"><i></i><i></i><i></i><i></i><i></i><i></i></div>
</section>

<section>
  <h1 class="abs display welcome-title" style="font-weight:400">Welcome to Quillmarsh</h1>
  <p class="abs body-copy welcome-copy">Lorem ipsum dolor sit amet, consectetur adipisicing elit, sed do eiusmod tempor incididunt ut labore et dolore magna aliqua. Ut enim ad minim veniam, quis nostrud exercitation ullamco laboris nisi ut aliquip ex ea commodo consequat. Duis aute irure dolor in reprehenderit in voluptate velit esse cillum dolore eu fugiat nulla pariatur. Excepteur sint occaecat cupidatat non proident, sunt in culpa qui officia deserunt mollit anim id est laborum.</p>
  <div class="abs btn btn-order">Order Now</div>

  <aside class="abs cases">
    <h2 class="display cases-head" style="font-weight:400">Case Studies &amp; Articles</h2>
    <p class="abs body-copy cases-copy">Lorem ipsum dolor sit amet, consectetur adipisicing elit, sed do eiusmod tempor incididunt ut labore et dolore magna aliqua. Ut enim ad minim veniam, quis nostrud exercitation ullamco laboris nisi ut aliquip ex ea commodo consequat. Duis aute irure... <span class="read-more">Read More..</span></p>
    <div class="abs cases-rule"></div>
    <ul class="abs cases-list">
      <li><span class="link">Lorem ipsum dolor sit amet</span></li>
      <li><span class="link">Lorem ipsum dolor sit amet</span></li>
      <li><span class="link">Lorem ipsum dolor sit amet</span></li>
      <li><span class="link">Lorem ipsum dolor sit amet</span></li>
    </ul>
  </aside>
</section>

<section class="abs products">
  <h2 class="abs display products-title" style="font-weight:400">Our Products</h2>
  <div class="abs product-badge" style="left:104px;top:62px">Orvane Play</div>
  <div class="abs product-badge" style="left:312px;top:62px">Kelto Soft</div>
  <div class="abs product-badge" style="left:522px;top:62px">Brimly TV</div>
  <p class="abs body-copy product-caption" style="left:72px;top:184px">Lorem ipsum dolor sit amet, consectetur adipisicing elit, sed do eiusmod tempor</p>
  <p class="abs body-copy product-caption" style="left:280px;top:184px">Lorem ipsum dolor sit amet, consectetur adipisicing elit, sed do eiusmod tempor</p>
  <p class="abs body-copy product-caption" style="left:491px;top:183px">Lorem ipsum dolor sit amet, consectetur adipisicing elit, sed do eiusmod tempor</p>
</section>

<section>
  <div class="abs video" role="img" aria-label="Video player showing a software development training video">
    <svg class="abs" style="left:101px;top:49px" width="70" height="70" viewBox="0 0 70 70"><circle cx="35" cy="35" r="35" fill="#000"/><polygon points="26,19 26,51 53,35" fill="#9a9a9a"/></svg>
    <div class="abs video-controls"></div>
  </div>
  <h2 class="abs display media-title" style="font-weight:400">Lorem Ipsum</h2>
  <p class="abs body-copy media-copy">Lorem ipsum dolor sit amet, consectetur adipisicing elit, sed do eiusmod tempor incididunt ut labore et dolore magna aliqua.</p>
  <div class="abs media-rule"></div>
  <div class="abs" style="left:495px;top:945px">
    <div class="display demo-label">Demo 1 :</div>
    <div class="demo-link"><span class="link">https://www.videoloop.example/watch?v=QSCfaTsCDrs</span></div>
    <div class="display demo-label">Demo 2 :</div>
    <div class="demo-link"><span class="link">https://www.videoloop.example/watch?v=jmeW5xLKXjY</span></div>
    <div class="display demo-label">Demo 3 :</div>
    <div class="demo-link"><span class="link">https://www.videoloop.example/watch?v=jmeW5xLKXjY</span></div>
  </div>
</section>

<footer>
  <div class="abs footer">
    <h3 class="abs display footer-title" style="font-weight:400">Partnership</h3>
    <div class="abs partner-card" style="left:54px;top:37px">Tessaline</div>
    <div class="abs partner-info" style="left:154px;top:41px">Tessaline Systems Corporation<br><span class="link">www.tessaline.example</span></div>
    <div class="abs footer-divider" style="left:260px"></div>
    <div class="abs partner-card" style="left:275px;top:37px">Marlowe</div>
    <div class="abs partner-info" style="left:376px;top:50px">Marlowe Corporation<br><span class="link">www.marlowe.example</span></div>
    <div class="abs footer-divider" style="left:483px"></div>
    <div class="abs partner-card" style="left:498px;top:37px">Ardenic</div>
    <div class="abs partner-info" style="left:601px;top:48px">Ardenic Micro Devices<br><span class="link">www.ardenic.example</span></div>
  </div>
  <div class="abs footer-bottom">
    <div class="abs copyright">©2014 Quillmarsh. All rights reserved.</div>
    <div class="abs display follow">Follow Us</div>
    <div class="abs follow-rule"></div>
    <span class="abs social" style="left:466px;background:#3b5998" aria-label="Social link"></span>
    <span class="abs social" style="left:492px;background:#3aa5dd" aria-label="Social link"></span>
    <span class="abs social" style="left:518px;background:#2a9fd8" aria-label="Social link"></span>
  </div>
</footer>

</body>
</html>
```